Brightpath Consulting WA Business Card

Create an interesting, eye catching and colourful two sided business card. We are a business consulting operation assisting SME's improve all areas of their business. We provide consulting services to assist SME's to create a culture of continuous improvement, making a positive difference in the business. Our tag line is Small changes, big rewards. We want to create a well recognised, innovative brand that can be continued throughout our website, social media and email correspondence.

Target Market(s)

Small to Medium Enterprise Business Owners

Industry/Entity Type

Business Consultant

Contact Information for Business Card

Name of Business: Brightpath Consulting - Small Changes Big Rewards
Dean Morrow Ph 0407358164 Lydia Morrow Ph 0409583417
Email brightpathconsultingwa@examplemail.com
Web address TBA
FaceBook page TBA

BACKSIDE OF CARD

Providing assistance with:

• Organisation & Efficiency
• Revenue generation & Marketing
• Financial Management
• Production quality & delivery
• Systems & Process documentation
• Exit Strategy

Font styles to use
Other font styles liked:
• Calibri

Colors

Designer to choose colors to be used in the design.

Requirements
Must have
• Calibri font

```html
<!DOCTYPE html>
<html lang="en">
<head>
<meta charset="utf-8">
<title>Brightpath Consulting – Business Card</title>
<link href="https://fonts.googleapis.com/css2?family=Carlito:wght@400;700&display=swap" rel="stylesheet">
<style>
  :root {
    --bg: #3a3a3c;
    --card: #ffffff;
    --blue: #0a72b5;
    --red: #e8402f;
    --ink: #1d1d1d;
    --white: #ffffff;
  }
  * { box-sizing: border-box; margin: 0; padding: 0; }
  html, body { width: 1200px; height: 1000px; overflow: hidden; }
  body {
    background: var(--bg);
    font-family: "Carlito", "Calibri", sans-serif;
    color: var(--ink);
    position: relative;
  }
  .card {
    position: absolute;
    left: 240px;
    width: 720px;
    height: 410px;
    background: var(--card);
    border-radius: 28px;
    overflow: hidden;
    box-shadow: 0 14px 30px rgba(0,0,0,.35);
  }
  .card--front { top: 50px; }
  .card--back { top: 530px; }

  .wave { position: absolute; inset: 0; width: 100%; height: 100%; }

  .brand {
    position: absolute;
    display: flex;
    align-items: center;
    gap: 12px;
  }
  .brand__mark {
    width: 22px; height: 22px; border-radius: 50%;
    background: var(--blue);
  }
  .brand__name {
    color: var(--red);
    font-weight: 700;
    text-transform: uppercase;
    letter-spacing: .5px;
    white-space: nowrap;
  }
  .card--front .brand { left: 58px; top: 150px; }
  .card--front .brand__name { font-size: 30px; }
  .front-tagline {
    position: absolute; left: 92px; top: 190px;
    font-size: 14px; font-weight: 700; text-transform: uppercase;
    letter-spacing: .4px;
  }
  .front-tagline .dot, .services .dot {
    display: inline-block; width: 8px; height: 8px; border-radius: 50%;
    background: var(--red); margin: 0 6px; vertical-align: middle;
  }

  .contacts { position: absolute; right: 46px; top: 90px; text-align: left; }
  .person { margin-bottom: 18px; }
  .person__name {
    color: var(--blue); font-weight: 700; font-size: 22px;
    text-transform: uppercase; letter-spacing: .6px; padding-left: 24px;
  }
  .person__phone { display: flex; align-items: center; gap: 6px; font-size: 22px; }
  .person__phone svg { width: 18px; height: 18px; fill: var(--blue); }

  .online {
    position: absolute; right: 40px; bottom: 26px;
    color: var(--white); font-size: 17px; text-align: right; line-height: 1.5;
  }
  .online__row { display: flex; align-items: center; justify-content: flex-end; gap: 8px; white-space: nowrap; }
  .online__row svg { width: 16px; height: 16px; fill: none; stroke: var(--white); stroke-width: 1.8; }

  .card--back .brand { left: 0; right: 0; top: 120px; justify-content: center; }
  .card--back .brand__name { font-size: 36px; }
  .back-tagline {
    position: absolute; left: 0; right: 0; top: 172px; text-align: center;
    color: var(--blue); font-weight: 700; font-size: 19px;
    text-transform: uppercase; letter-spacing: .5px;
  }
  .services {
    position: absolute; left: 20px; right: 20px; top: 250px;
    text-align: center; font-size: 18px; line-height: 1.7;
  }
  .services__line { display: block; white-space: nowrap; }
</style>
</head>
<body>

  <section class="card card--front" aria-label="Card front">
    <svg class="wave" viewBox="0 0 720 410" preserveAspectRatio="none" aria-hidden="true">
      <path d="M0,215 C120,262 250,292 380,296 C280,300 130,278 0,240 Z" fill="var(--red)"/>
      <path d="M0,255 C140,310 280,328 400,318 C520,306 600,276 720,272 L720,410 L0,410 Z" fill="var(--blue)"/>
    </svg>

    <div class="brand">
      <span class="brand__mark"></span>
      <span class="brand__name">Brightpath Consulting</span>
    </div>
    <p class="front-tagline">Small changes<span class="dot"></span>Big rewards</p>

    <div class="contacts">
      <div class="person">
        <p class="person__name">Dean Morrow</p>
        <p class="person__phone"><svg viewBox="0 0 24 24"><path d="M6.6 10.8a15 15 0 0 0 6.6 6.6l2.2-2.2a1 1 0 0 1 1-.25 11.4 11.4 0 0 0 3.6.57 1 1 0 0 1 1 1V20a1 1 0 0 1-1 1A17 17 0 0 1 3 4a1 1 0 0 1 1-1h3.5a1 1 0 0 1 1 1c0 1.25.2 2.45.57 3.570a1 1 0 0 1-.25 1z"/></svg>0407 358 164</p>
      </div>
      <div class="person">
        <p class="person__name">Lydia Morrow</p>
        <p class="person__phone"><svg viewBox="0 0 24 24"><path d="M6.6 10.8a15 15 0 0 0 6.6 6.6l2.2-2.2a1 1 0 0 1 1-.25 11.4 11.4 0 0 0 3.6.57 1 1 0 0 1 1 1V20a1 1 0 0 1-1 1A17 17 0 0 1 3 4a1 1 0 0 1 1-1h3.5a1 1 0 0 1 1 1c0 1.25.2 2.45.57 3.57a1 1 0 0 1-.25 1z"/></svg>0409 583 417</p>
      </div>
    </div>

    <div class="online">
      <p class="online__row">info@brightpathconsulting.example<svg viewBox="0 0 24 24"><rect x="3" y="6" width="18" height="12" rx="1"/><path d="M3 6l9 7 9-7"/></svg></p>
      <p class="online__row">www.brightpathconsulting.example<svg viewBox="0 0 24 24"><circle cx="12" cy="12" r="9"/><path d="M3 12h18M12 3c3 3 3 15 0 18M12 3c-3 3-3 15 0 18"/></svg></p>
    </div>
  </section>

  <section class="card card--back" aria-label="Card back">
    <div class="brand">
      <span class="brand__mark"></span>
      <span class="brand__name">Brightpath Consulting</span>
    </div>
    <p class="back-tagline">Creating a culture of continuous improvement</p>
    <p class="services">
      <span class="services__line">Organisation &amp; Efficiency<span class="dot"></span>Revenue generation &amp; Marketing<span class="dot"></span>Financial Management</span>
      <span class="services__line">Production quality &amp; delivery<span class="dot"></span>Systems &amp; Process documentation<span class="dot"></span>Exit Strategy</span>
    </p>
  </section>

</body>
</html>
```